We are looking for a new website design for our SEO WEB Development Company. The URL is www.brellowcreativeworks.com

We want it to be a more powerful representation of what we do. We are also looking for a number of designers that we will give continuous business to every month. The persons design we choose will also get a proposal to complete 4 - 6 new designs for us every month for our clients.

Be creative as you can in your design submissions. We really want to stand out!

Just to give you an idea of what we like look at this site: http://www.tovandigitalstudio.com/

```html
<!DOCTYPE html>
<html lang="en">
<head>
<meta charset="utf-8">
<title>Brellow Interactive Group</title>
<link rel="stylesheet" href="https://fonts.googleapis.com/css2?family=Roboto:wght@400;500;700&family=Roboto+Condensed:wght@500&family=Crimson+Text:wght@400;700&display=swap">
<style>
:root{
  --navy:#0f4c7e;
  --title-blue:#1463a0;
  --ink:#2b2b2b;
  --band:#ececec;
  --footer:#202020;
}
*{box-sizing:border-box;margin:0;padding:0}
html,body{width:870px;height:1200px;overflow:hidden}
body{position:relative;background:#fff;font-family:"Roboto",Arial,sans-serif;color:var(--ink)}
.abs{position:absolute}

.topbar{left:0;top:0;width:870px;height:34px;background:var(--navy);color:#fff;font-size:11px}
.topbar .call{position:absolute;left:521px;top:10px;font-weight:700;font-size:12px}
.topbar .divider{position:absolute;left:658px;top:5px;width:1px;height:24px;background:#6f97b8}
.topbar .links{position:absolute;left:671px;top:10px;word-spacing:1px}
.topbar .links span{color:#8fb0cc;margin:0 4px}

.brand{left:28px;top:72px;font-size:24px;font-weight:500;color:var(--ink);line-height:28px}

.mainnav{left:331px;top:77px;font-size:15.5px;color:#111;display:flex;gap:21px}

.hero{left:0;top:139px;width:870px;height:254px;background:var(--band)}
.shot{left:34px;top:155px;width:322px;height:220px;background:linear-gradient(#cfcfcf 0,#cfcfcf 30px,#111 30px,#0b0b0b);box-shadow:0 6px 8px rgba(0,0,0,.35)}
.hero-title{left:382px;top:167px;font-size:15.5px;font-weight:500;color:#222}
.hero-copy{left:382px;top:214px;width:182px;font-size:11.5px;line-height:14.3px;color:#333}
.dots{left:383px;top:303px;display:flex;gap:5px}
.dots i{width:8px;height:8px;border-radius:50%;background:#888}
.dots i:last-child{background:#222}

.quote{left:622px;top:154px;width:221px;height:349px;background:#fff;border:1px solid #d4d4d4}
.quote .head{height:79px;background:linear-gradient(#1e5f92,#164f7f);color:#fff;text-align:center;font-family:"Crimson Text",Georgia,serif;padding-top:10px;position:relative}
.quote .head b{display:block;font-size:16px;line-height:17px}
.quote .head span{display:block;font-size:15.5px;line-height:18px}
.quote .head:after{content:"";position:absolute;left:105px;bottom:-6px;border:6px solid transparent;border-bottom:0;border-top-color:#164f7f}
.field{position:absolute;left:11px;width:195px}
.field label{display:block;font-size:10px;font-weight:700;color:#333}
.field .input{margin-top:7px;height:24px;border:1px solid #d6d6d6;box-shadow:inset 0 1px 2px rgba(0,0,0,.08);background:#fff}
.quote .rule{position:absolute;left:0;top:311px;width:100%;height:1px;background:#ddd}
.quote .btn{position:absolute;left:16px;top:316px;width:188px;height:27px;border-radius:3px;background:linear-gradient(#fbb132,#ef8a12);color:#fff;font-size:13px;font-weight:700;text-align:center;line-height:27px}

.intro{left:28px;top:425px;width:582px;font-size:14px;line-height:17.5px;color:#333}
.intro b{font-weight:500;color:#222}

.services{left:0;top:522px;width:870px;height:390px;background:#ececec;border-top:1px solid #ddd}
.card{width:379px;height:159px;background:linear-gradient(#fff,#eeeeee);border:1px solid #d2d2d2}
.card svg{position:absolute;left:13px;top:14px}
.card h2{position:absolute;left:66px;top:11px;font-family:"Roboto Condensed","Arial Narrow",sans-serif;font-weight:500;font-size:17.5px;color:var(--title-blue);text-transform:uppercase}
.card p{position:absolute;left:66px;top:39px;width:300px;font-size:10px;line-height:12.3px;color:#333}

.footer{left:0;top:912px;width:870px;height:288px;background:var(--footer);color:#fff}
.footer h3{position:absolute;top:32px;font-size:14px;font-weight:500;letter-spacing:.5px}
.fcol{position:absolute;top:71px;font-size:10px;line-height:12.3px;color:#eee}
.fcol h4{font-size:10px;font-weight:700;letter-spacing:.2px}
.fcol .gap{height:13px}
.footer .rule{position:absolute;left:28px;top:243px;width:815px;height:1px;background:#3d3d3d}
.footer .copy{position:absolute;right:27px;top:260px;font-size:9.5px;color:#ddd}
</style>
</head>
<body>

<header>
  <div class="abs topbar">
    <div class="call">Call us: 555-014-2290</div>
    <div class="divider"></div>
    <div class="links">About Us<span>|</span>Our Work<span>|</span>Contact Us</div>
  </div>
  <div class="abs brand">Brellow Interactive Group</div>
  <nav class="abs mainnav">
    <span>Creative Design</span><span>Website Design</span><span>Internet Marketing</span><span>IT Consulting</span>
  </nav>
</header>

<section class="abs hero"></section>
<div class="abs shot" role="img" aria-label="Browser screenshot of a photography portfolio website project"></div>
<h1 class="abs hero-title">Mara Lindquist Photography</h1>
<p class="abs hero-copy">Lorem ipsum dolor sit amet, con-sectetur adipisicing elit, sed do eiusmod tempor incididunt ut labore et dolore magna aliqua.</p>
<div class="abs dots"><i></i><i></i><i></i></div>

<form class="abs quote">
  <div class="head"><b>Get A Free</b><span>Reputation Management &amp;</span><span>Repair Quote!</span></div>
  <div class="field" style="top:96px"><label>Name</label><div class="input"></div></div>
  <div class="field" style="top:148px"><label>Phone Number</label><div class="input"></div></div>
  <div class="field" style="top:202px"><label>Email</label><div class="input"></div></div>
  <div class="field" style="top:254px"><label>Website Address</label><div class="input"></div></div>
  <div class="rule"></div>
  <div class="btn">Request For Quote</div>
</form>

<p class="abs intro"><b>Brellow Interactive Group</b> is a leading Harlow Web Site Design, Publishing and Internet Marketing Firm. Our Harlow Texas based Website Design and Internet Marketing experts are some of the best in the industry!</p>

<section class="abs services"></section>

<article class="abs card" style="left:27px;top:546px">
  <svg width="38" height="38" viewBox="0 0 38 38"><circle cx="19" cy="19" r="17" fill="#2b7fd0"/><ellipse cx="19" cy="19" rx="8" ry="17" fill="none" stroke="#cfe6ff" stroke-width="1.2"/><path d="M2 19h34M5 10h28M5 28h28" stroke="#cfe6ff" stroke-width="1.2"/></svg>
  <h2>Brellow Interactive Web</h2>
  <p>is a full-service Harlow based Advertising Agency comprised of experienced advertising and marketing professionals that provide clients with a clear and distinct voice in the marketplace. Web Site Design and Internet Marketing experts at our Harlow location specialize in developing Online Marketing Strategies, Search Engine Marketing and Optimization (SEO), Pay Per Click , Web Site Design and Development, and Online Reputation Management.</p>
</article>

<article class="abs card" style="left:465px;top:546px">
  <svg width="38" height="38" viewBox="0 0 38 38"><rect x="2" y="4" width="34" height="28" rx="2" fill="#e9eef3" stroke="#8a97a4"/><rect x="2" y="4" width="34" height="6" fill="#b9c4cf"/><circle cx="19" cy="21" r="7" fill="#2b7fd0"/></svg>
  <h2>Brellow Interactive Publishing</h2>
  <p>provides full-service custom publishing and consulting services for magazines, newsletters, blogs and web sites. We are the complete interactive publishing arm for your organization. Our services include: Strategic Planning and Computer Modeling; Art Direction and Design; Production Services; Circulation Market-ing and Management; Subscription Fulfillment Management; Advertising Sales Management; Web Site and Digital Magazine Design and Management; and Video Streaming Services.</p>
</article>

<article class="abs card" style="left:27px;top:737px">
  <svg width="38" height="38" viewBox="0 0 38 38"><rect x="2" y="3" width="34" height="25" rx="2" fill="#cfd6dd"/><rect x="5" y="6" width="28" height="19" fill="#2b7fd0"/><rect x="15" y="28" width="8" height="4" fill="#9aa5b0"/><rect x="10" y="32" width="18" height="3" rx="1" fill="#9aa5b0"/></svg>
  <h2>Brellow Interactive Media</h2>
  <p>provides cost-effective Web Site Design services, Search Engine Marketing, Internet Advertising, Internet Marketing Campaigns and most important, we can accommodate any budget.</p>
</article>

<article class="abs card" style="left:465px;top:737px">
  <svg width="38" height="38" viewBox="0 0 38 38"><circle cx="19" cy="19" r="17" fill="#d42a2a"/><circle cx="19" cy="19" r="8" fill="#fff"/><path d="M19 2v9M19 27v9M2 19h9M27 19h9" stroke="#fff" stroke-width="5"/></svg>
  <h2>Reputation Management and Repair</h2>
  <p>We offer a plan of action to create a process of tracking an entity's actions and other entities' opinions about those actions; reporting on those actions and opinions; and reacting to that report creating a feedback loop. Reputation management has become essential with the advent of widespread computing. Reputation management systems use predefined criteria for processing complex data to report the many factors affecting a company's reputation. However, these systems only facilitate and automate the process of determining trustworthiness.</p>
</article>

<footer class="abs footer">
  <h3 style="left:28px">CONTACT</h3>
  <h3 style="left:331px">SITE MAP</h3>
  <div class="fcol" style="left:28px">
    <h4>NORTHFIELD LOCATION</h4>
    Brellow Interactive Group<br>47 Quillfern Lane<br>Northfield, Texas 75590
    <div class="gap"></div>
    <h4>HARLOW LOCATION</h4>
    Brellow Interactive Group<br>2200 Ashcombe Parkway<br>Harlow, TX 75580-1140<br><b>Phone:</b> 555-014-2290
  </div>
  <div class="fcol" style="left:331px">
    <h4>CREATIVE DESIGN</h4>
    Creative Advertising<br>Print Design<br>Corporate Identity<br>Packaging
    <div class="gap"></div>
    <h4>WEBSITE DESIGN</h4>
    Web Design<br>E-commerce<br>Multimedia<br>Web Application Development
  </div>
  <div class="fcol" style="left:516px">
    <h4>INTERNET MARKETING</h4>
    Search Engine Optimization<br>SEM and Pay-per-Click<br>Email Marketing<br>SEO Copywriting<br>Reputation Repair &amp; Management
    <div class="gap"></div>
    <h4>IT CONSULTING</h4>
  </div>
  <div class="fcol" style="left:717px">
    <h4>BRELLOW INTERACTIVE</h4>
    About Us<br>Our Work<br>Contact Us
  </div>
  <div class="rule"></div>
  <div class="copy">© 2011 Brellow Interactive. All Rights Reserved.</div>
</footer>

</body>
</html>
```